Visitenkarte erstellen für Reiki Praxis

Visitenkarten für Reiki Praxis Doppelseitig

business cards reiki practice double-sided

The background can also be a different color

```html
<!DOCTYPE html>
<html lang="en">
<head>
<meta charset="utf-8">
<title>Quiet Current – Business Cards</title>
<link rel="stylesheet" href="https://fonts.googleapis.com/css2?family=Questrial&family=Open+Sans:wght@500&display=swap">
<style>
  :root {
    --page-bg: #2b2b2b;
    --card-black: #050505;
    --card-back: #0a0a0a;
    --pattern-tone: #161616;
    --band-white: #f1f1f1;
    --ink-white: #f4f4f4;
    --ink-dark: #1c1c1c;
    --gold: #d6a23c;
    --rule: #7a5a3a;
  }
  * { box-sizing: border-box; margin: 0; padding: 0; }
  html, body { width: 1200px; height: 732px; overflow: hidden; }
  body { background: var(--page-bg); position: relative; font-family: "Questrial", sans-serif; }

  .card {
    position: absolute; top: 242px; width: 436px; height: 248px;
    overflow: hidden; box-shadow: 0 6px 14px rgba(0,0,0,.45);
  }
  .card--front { left: 144px; background: var(--card-black); }
  .card--back { left: 621px; background: var(--card-back); }

  .brand-mark {
    position: absolute; left: 50%; transform: translateX(-50%);
    width: 34px; height: 34px; border: 1.5px solid var(--gold); border-radius: 50%;
  }
  .brand-name {
    position: absolute; left: 0; width: 100%; text-align: center;
    font-family: "Open Sans", sans-serif; font-weight: 500;
    color: var(--ink-white); letter-spacing: .5px;
  }
  .card--front .brand-mark { top: 22px; }
  .card--front .brand-name { top: 66px; font-size: 17px; }

  .front-rule {
    position: absolute; left: 23px; top: 119px; width: 390px; height: 1px; background: var(--rule);
  }
  .person { position: absolute; left: 23px; top: 148px; width: 180px; text-align: right; color: var(--ink-white); }
  .person__name { font-size: 18px; letter-spacing: .6px; line-height: 22px; text-align: left; }
  .person__role { font-size: 11.5px; line-height: 14px; }
  .front-divider { position: absolute; left: 211px; top: 146px; width: 1px; height: 42px; background: var(--gold); }

  .contacts { position: absolute; left: 224px; top: 142px; list-style: none; color: var(--ink-white); font-size: 11.5px; }
  .contacts li { display: flex; align-items: center; height: 14.5px; }
  .contacts svg { width: 10px; height: 10px; margin-right: 8px; flex: none; }

  .address-band {
    position: absolute; left: 0; bottom: 0; width: 100%; height: 38px; background: var(--band-white);
    color: var(--ink-dark); font-size: 12px; display: flex; align-items: center; justify-content: center;
  }

  .back-pattern {
    position: absolute; inset: 0;
    background: linear-gradient(160deg, var(--pattern-tone), var(--card-back) 70%);
  }
  .brand-block { position: absolute; left: 259px; top: 130px; width: 120px; height: 90px; }
  .brand-block .brand-mark { top: 12px; }
  .brand-block .brand-name { top: 64px; font-size: 9.5px; }
</style>
</head>
<body>
  <section class="card card--front" aria-label="Business card front">
    <div class="brand-mark"></div>
    <p class="brand-name">QUIET CURRENT</p>
    <div class="front-rule"></div>
    <div class="person">
      <p class="person__name">MARA LINDQVIST</p>
      <p class="person__role">Owner</p>
    </div>
    <div class="front-divider"></div>
    <ul class="contacts">
      <li>
        <svg viewBox="0 0 10 10"><path d="M2 1 L3.6 1 L4.2 3 L3.1 3.8 Q4 5.8 6.2 6.9 L7 5.8 L9 6.4 L9 8 Q8.6 9 7.5 9 Q1 8 1 2.5 Q1 1.4 2 1Z" fill="var(--gold)"/></svg>
        555-014-2277
      </li>
      <li>
        <svg viewBox="0 0 10 10"><rect x="0.5" y="2" width="9" height="6.5" fill="var(--gold)"/><path d="M0.5 2 L5 5.6 L9.5 2" stroke="var(--card-black)" stroke-width="0.9" fill="none"/></svg>
        mara@quietcurrent.com
      </li>
      <li>
        <svg viewBox="0 0 10 10"><circle cx="5" cy="5" r="4.3" fill="var(--gold)"/><g stroke="var(--card-black)" stroke-width=".7" fill="none"><ellipse cx="5" cy="5" rx="1.8" ry="4.3"/><path d="M0.7 5 H9.3 M1.4 3 H8.6 M1.4 7 H8.6"/></g></svg>
        www.quietcurrent.com
      </li>
    </ul>
    <div class="address-band">12 Harbor Lane, Bayview, FL 00000</div>
  </section>

  <section class="card card--back" aria-label="Business card back">
    <div class="back-pattern" role="img" aria-label="Faint repeating brand-name pattern across the card back"></div>
    <div class="brand-block">
      <div class="brand-mark"></div>
      <p class="brand-name">QUIET CURRENT</p>
    </div>
  </section>
</body>
</html>
```